Brovelline International is looking for web design

I have a website that I made myself and I wanted to have a more professional design. go to my website www.BrovellinePX.example and you will see what it is all about. My website was created with Weebly. we like to focus on that we have an earth friendly product. we offer a natural alternative to asphalt or concrete .

Target Market(s)

Landscape Archtects, Home Improvement , designers, parks and recreation

Industry/Entity Type

It Professional

Coding

Coded - Design and coding required

Number of Pages Required

5+ page

Requirements
Must have
• Landing page,
• Products Page contact us page

```html
<!DOCTYPE html>
<html lang="en">
<head>
<meta charset="utf-8">
<title>Brovelline International – Contact Us</title>
<link href="https://fonts.googleapis.com/css2?family=League+Gothic&family=PT+Sans:ital,wght@0,400;0,700;1,400&family=Open+Sans:wght@400;600&display=swap" rel="stylesheet">
<style>
:root{
  --green:#7cbd3c;
  --brown:#6e564a;
  --rust:#8a3a25;
  --nav:#a39468;
  --panel:#d4c9ad;
  --field:#f5eedc;
  --footer:#6b7788;
  --grey:#7a7a7a;
  --white:#ffffff;
}
*{box-sizing:border-box;margin:0;padding:0}
html,body{width:978px;height:1200px;overflow:hidden;background:var(--white)}
body{position:relative;font-family:"PT Sans",sans-serif}
.abs{position:absolute}

.site-header{left:0;top:0;width:978px;height:111px}
.brand{left:62px;top:36px;display:flex;align-items:center;gap:10px}
.brand-dot{width:30px;height:30px;border-radius:50%;background:var(--green)}
.brand-name{font-family:"PT Sans",sans-serif;font-weight:700;font-size:23px;color:var(--green);letter-spacing:.5px}
.main-nav a{position:absolute;top:62px;font-family:"PT Sans",sans-serif;font-weight:700;font-size:12px;color:var(--nav);text-decoration:none;white-space:nowrap}
.main-nav a.active{color:var(--rust)}
.nav-marker{left:431px;top:106px;width:43px;height:5px;background:var(--rust)}

.hero{left:0;top:111px;width:978px;height:235px;background:linear-gradient(100deg,#4f7a34 0%,#6d9447 35%,#8fa37a 55%,#557f3a 75%,#3f6a2c 100%)}
.hero-tab{left:61px;top:346px;width:270px;height:15px;background:#5b8a3a}
.hero-title{right:61px;top:226px;text-align:right;font-family:"League Gothic",sans-serif;font-size:36px;line-height:34px;color:var(--white)}

.call-line{right:61px;top:356px;font-family:"League Gothic",sans-serif;font-size:24px;color:var(--brown);letter-spacing:.5px}
.call-line span{color:var(--rust)}

.page-title{left:86px;top:400px;font-family:"League Gothic",sans-serif;font-size:30px;color:var(--brown);letter-spacing:.5px}
.intro{left:86px;top:451px;width:200px;font-size:11.5px;line-height:18px;color:#333}

.side-heading{left:85px;font-family:"League Gothic",sans-serif;font-size:19px;color:var(--brown);letter-spacing:.5px}
.side-bar{left:85px;width:171px;height:7px;background:var(--green)}
.address{left:85px;top:616px;font-size:13.5px;line-height:19.6px;color:var(--grey)}
.map{left:85px;top:763px;width:173px;height:226px;background:#ecd9cc}

.form-panel{left:354px;top:454px;width:563px;height:537px;background:var(--panel)}
.form-heading{left:404px;top:498px;font-family:"League Gothic",sans-serif;font-size:22px;color:var(--white);letter-spacing:.8px}
.field{position:absolute;background:var(--field);font-style:italic;font-size:11.5px;color:#3a3a3a;padding:8px 8px}
.submit{left:406px;top:938px;width:95px;height:24px;background:var(--green);color:var(--white);font-weight:700;font-size:11.5px;letter-spacing:1px;display:flex;align-items:center;justify-content:center}

.site-footer{left:0;top:1042px;width:978px;height:158px;background:var(--footer);color:var(--white);font-family:"Open Sans",sans-serif}
.footer-address{left:78px;top:47px;font-size:9.5px}
.divider{top:34px;width:1px;height:42px;background:#8b96a5}
.footer-phone{left:410px;top:38px;font-size:21px;display:flex;align-items:center;gap:6px}
.footer-mail{left:653px;top:46px;font-size:10px;display:flex;align-items:center;gap:10px}
.social{left:835px;top:48px;display:flex;gap:6px}
.social span{width:12px;height:12px;border:1px solid var(--white);border-radius:50%}
.copyright{left:0;width:978px;top:80px;text-align:center;font-size:8.5px}
</style>
</head>
<body>

<header class="site-header abs">
  <div class="brand abs">
    <div class="brand-dot"></div>
    <div class="brand-name">Brovelline International</div>
  </div>
  <nav class="main-nav">
    <a class="active" style="left:437px">HOME</a>
    <a style="left:490px">PRODUCTS</a>
    <a style="left:568px">ASK THE EXPERTS</a>
    <a style="left:683px">DISTRIBUTORS</a>
    <a style="left:782px">CONTACT US</a>
    <a style="left:869px">MEDIA</a>
  </nav>
  <div class="nav-marker abs"></div>
</header>

<div class="hero abs" role="img" aria-label="Photo of a winding paved garden path through lush green trees and shrubs"></div>
<div class="hero-tab abs" role="img" aria-label="Lower edge of the garden path photo"></div>
<h1 class="hero-title abs">THE BEST NATURAL<br>PAVING SYSTEM</h1>

<div class="call-line abs">CALL <span>555.014.2736</span> NOW!</div>

<h2 class="page-title abs">CONTACT US</h2>
<p class="intro abs">If you are interested in our products or require more information, please get in touch with us by sending the form or give us a call..</p>

<h3 class="side-heading abs" style="top:569px">ADDRESS</h3>
<div class="side-bar abs" style="top:591px"></div>
<address class="address abs" style="font-style:normal">Brovelline Intl.,<br>418 Fennick Ridge Road,<br>Alder Vale,<br>CA 90217</address>

<h3 class="side-heading abs" style="top:719px">LOCATION</h3>
<div class="side-bar abs" style="top:742px"></div>
<div class="map abs" role="img" aria-label="Street map showing the office location"></div>

<section class="form-panel abs"></section>
<h2 class="form-heading abs">LET US KNOW HOW WE CAN HELP..</h2>
<div class="field" style="left:404px;top:550px;width:219px;height:31px">First Name</div>
<div class="field" style="left:646px;top:550px;width:220px;height:31px">Last Name</div>
<div class="field" style="left:404px;top:611px;width:316px;height:31px">Company Name</div>
<div class="field" style="left:404px;top:671px;width:73px;height:31px">Phone #</div>
<div class="field" style="left:500px;top:671px;width:74px;height:31px"></div>
<div class="field" style="left:598px;top:671px;width:122px;height:31px"></div>
<div class="field" style="left:404px;top:732px;width:316px;height:30px">Email</div>
<div class="field" style="left:404px;top:792px;width:465px;height:115px">Message</div>
<div class="submit abs">SUBMIT</div>

<footer class="site-footer abs">
  <div class="footer-address abs">Brovelline Intl., 418 Fennick Ridge Road, Alder Vale, CA 90217</div>
  <div class="divider abs" style="left:354px"></div>
  <div class="footer-phone abs">
    <svg width="18" height="18" viewBox="0 0 18 18" fill="none" stroke="#fff" stroke-width="1.2"><circle cx="9" cy="9" r="8"/><path d="M6 5.5l1.3-.5 1 2-.9.8a5 5 0 0 0 2.8 2.8l.8-.9 2 1-.5 1.3c-3 .3-6.8-3.5-6.5-6.5z"/></svg>
    555.014.2736
  </div>
  <div class="divider abs" style="left:624px"></div>
  <div class="footer-mail abs">
    <svg width="13" height="9" viewBox="0 0 13 9" fill="none" stroke="#fff" stroke-width="1"><rect x=".5" y=".5" width="12" height="8"/><path d="M.5.5l6 4.5 6-4.5"/></svg>
    info@brovelline.example
  </div>
  <div class="divider abs" style="left:794px"></div>
  <div class="social abs"><span></span><span></span><span></span></div>
  <div class="copyright abs">© Copyright 2016 Brovelline International, All rights reserved</div>
</footer>

</body>
</html>
```